Velmora Template Design for Wordpress Brightpath Site

We need graphic design and theme design work for our new site that will be running Brightpath with Velmora as the theme.

We have a draft logo that needs a graphic designer to improve it.

We are looking for sleek, modern, design that while minimal is distinct. ie page elements, content enhancement, block design that can be used, reused by in-house team.
This means there will also need to be a guide created on how to create, insert, edit each of those elements so that they can be used on new pages over time.

We have several businesses for which this is the "umbrella company" and so we will want to unify the colours and have identified a palette from which to start.

Some examples of site design we would like to stand up like:
https://www.tovrix.example/
https://pallorbranding.example/
https://business.skolvane.example/
https://www.fenwarrow.example/learning/home.aspx

When I say "coded" below, this really just means the CSS needed for page elements.

Target Market(s)

Small firms in professional services - engineers, land surveyors, consultants

Number of Pages Required

3 page

Font styles to use
Sans Serif

Requirements
Must have
• Wordpress/Velmora as base template, full home page layout with lorem ipsum placeholder
Nice to have
• custom blocks for pull quotes, call to action, a better design on the logo so it doesn't look like a rainbow.
Should not have
• Need for Structivo

```html
<!DOCTYPE html>
<html lang="en">
<head>
<meta charset="utf-8">
<title>Corvanta – Real Time Operational Intelligence</title>
<link rel="stylesheet" href="https://fonts.googleapis.com/css2?family=Poppins:wght@400;500;600;700&display=swap">
<style>
:root{
  --ink:#111111;
  --text:#333333;
  --muted:#8a8a8a;
  --panel:#f1f1f1;
  --line:#e6e6e6;
  --orange:#f7941d;
  --orange-deep:#f26b21;
  --purple:#5a3a96;
  --navy:#374a7b;
  --yellow:#fdc31a;
  --green:#6fa84a;
  --teal:#13a7b8;
  --white:#ffffff;
}
*{box-sizing:border-box;margin:0;padding:0}
html,body{width:1200px;height:4418px;overflow:hidden;background:var(--white)}
body{font-family:'Poppins',sans-serif;color:var(--text);position:relative}
.abs{position:absolute}
.btn{position:absolute;display:flex;align-items:center;justify-content:center;border-radius:22px;font-size:10px;font-weight:600;color:var(--white);background:linear-gradient(90deg,var(--orange),var(--orange-deep))}
.btn--mix{background:linear-gradient(90deg,var(--orange),var(--purple))}
.btn--ghost{background:var(--white);color:var(--ink);border:1.5px solid #e2c6a0}
.brand{font-weight:500;color:var(--ink);display:flex;align-items:center;gap:6px}
.brand__dot{width:10px;height:10px;border-radius:50%;background:var(--orange)}

/* header */
.nav{position:absolute;top:30px;left:430px;display:flex;gap:27px;font-size:10px;font-weight:600;color:var(--ink)}

/* hero */
.hero-title{left:130px;top:146px;font-size:43px;font-weight:700;line-height:1.03;color:var(--ink);width:520px}
.hero-copy{left:130px;top:295px;width:400px;font-size:9.5px;line-height:1.65}
.hero-photo{left:585px;top:72px;width:615px;height:506px;background:linear-gradient(135deg,#d9d4cc,#8b7d72 60%,#3a3330);clip-path:polygon(22% 0,100% 0,100% 100%,0 100%,0 40%)}
.hero-badge{left:600px;top:278px;width:100px;height:100px;border-radius:50%;background:var(--white);box-shadow:0 4px 18px rgba(0,0,0,.12);display:flex;align-items:center;justify-content:center;font-size:19px}

/* colour bands */
.color-band{position:absolute;background:linear-gradient(90deg,var(--yellow),var(--green) 25%,var(--navy) 45%,var(--purple) 60%,var(--teal) 78%,var(--yellow))}

/* about */
.about-photo{left:137px;top:677px;width:483px;height:337px;border-top-left-radius:330px 337px;background:linear-gradient(135deg,#e7e0d8,#9a8b7e 55%,#50433d)}
.photo-accent{position:absolute;width:104px;height:104px;border-radius:50%;background:linear-gradient(135deg,var(--yellow),var(--green) 50%,var(--navy))}
.eyebrow-dot{width:14px;height:14px;border-radius:50%;background:var(--teal)}
.h2{font-size:32px;font-weight:600;line-height:1.15;color:var(--ink)}
.body{font-size:9.5px;line-height:1.7}

/* expertise */
.panel{position:absolute;left:0;width:1200px;background:var(--panel);border-radius:90px}
.exp-item{position:absolute;top:1305px;width:100px;text-align:center;font-size:10.5px;font-weight:600;color:var(--ink);line-height:1.35}
.exp-icon{width:56px;height:56px;margin:0 auto 10px;border-radius:50%;background:var(--white);display:flex;align-items:center;justify-content:center}
.exp-icon span{width:24px;height:24px;border-radius:6px}
.dome{left:450px;top:1487px;width:300px;height:203px;background:var(--white);border-radius:150px 150px 0 0;display:flex;align-items:center;justify-content:center;padding-top:20px;font-size:24px}

/* courses */
.card{position:absolute;width:285px;height:393px;border:1px solid var(--line);border-radius:8px;background:var(--white)}
.card__img{position:absolute;left:7px;top:7px;width:269px;height:212px;border-radius:4px}
.card__tag{position:absolute;left:14px;top:16px;font-size:7px;color:var(--white);padding:3px 9px;border-radius:10px}
.card__ring{position:absolute;left:228px;top:196px;width:34px;height:34px;border-radius:50%;background:var(--white);border:3px solid var(--green);font-size:7.5px;font-weight:600;display:flex;align-items:center;justify-content:center;color:var(--text)}
.card__lessons{position:absolute;left:18px;top:240px;font-size:6.5px;color:var(--white);background:#cfcfcf;padding:3px 10px;border-radius:10px}
.card__price{position:absolute;right:14px;top:236px;font-size:12px;font-weight:500;color:var(--ink)}
.card__title{position:absolute;left:18px;top:270px;font-size:11px;font-weight:600;color:var(--ink)}
.card__author{position:absolute;left:18px;top:293px;font-size:7.5px;display:flex;align-items:center;gap:6px}
.card__author i{width:16px;height:16px;border-radius:50%;background:var(--yellow);display:block}
.card__text{position:absolute;left:18px;top:318px;width:245px;font-size:9px;line-height:1.65}

/* testimonials */
.ghost-word{left:0;width:1200px;top:2950px;text-align:center;font-size:96px;font-weight:700;line-height:1;color:#dedede;letter-spacing:2px;z-index:1}
.quote-card{left:226px;top:3034px;width:748px;height:322px;background:var(--white);border-radius:28px;z-index:2}
.quote-photo{left:266px;top:3034px;width:316px;height:322px;background:linear-gradient(180deg,#e9e6e2,#cfc9c2);z-index:3}
.quote-body{z-index:3}

/* footer */
.foot-h{font-size:14px;font-weight:600;color:var(--ink)}
.foot-list{font-size:9.5px;line-height:2.6}
</style>
</head>
<body>

<!-- header -->
<div class="abs brand" style="left:130px;top:20px;font-size:30px">Corvanta<span class="brand__dot"></span></div>
<nav class="nav"><span>Home</span><span>About Us</span><span>Services</span><span>Courses</span><span>Contact</span></nav>
<div class="btn" style="left:940px;top:17px;width:128px;height:38px">Get Started</div>

<!-- hero -->
<div class="hero-photo abs" role="img" aria-label="Photo of a smiling team of young professionals gathered around a laptop, with yellow leaf accents"></div>
<div class="hero-badge abs brand">Corvanta</div>
<h1 class="hero-title abs">Real Time Operational Intelligence for Professional Firms</h1>
<p class="hero-copy abs">Corvanta provides real-time operational intelligence for professional firms, helping businesses streamline their operations, training programs, and team management under a single, modern platform. With our solutions, firms can enhance efficiency, improve collaboration, and stay ahead in today's competitive landscape.</p>
<div class="btn btn--mix" style="left:130px;top:400px;width:128px;height:40px">Explore Services</div>
<div class="btn btn--ghost" style="left:266px;top:400px;width:128px;height:40px">View Courses</div>

<div class="color-band" style="left:0;top:510px;width:585px;height:68px" role="img" aria-label="Decorative band of multicoloured geometric shapes"></div>

<!-- about -->
<div class="about-photo abs" role="img" aria-label="Photo of a diverse team meeting around a round table with laptops"></div>
<div class="photo-accent" style="left:567px;top:934px" role="img" aria-label="Decorative multicoloured accent shape"></div>
<div class="abs eyebrow-dot" style="left:698px;top:716px"></div>
<h2 class="abs h2" style="left:698px;top:748px;width:360px">Empowering Small Professional Firms</h2>
<p class="abs body" style="left:698px;top:837px;width:360px">Corvanta is the umbrella company for professional service firms, providing seamless solutions for engineers, consultants, and land surveyors. Our platform unifies branding, training, and operational intelligence for modern business needs.</p>
<div class="btn" style="left:698px;top:920px;width:128px;height:40px">Read More</div>

<!-- expertise -->
<div class="panel" style="top:1137px;height:553px"></div>
<h2 class="abs h2" style="left:0;width:1200px;text-align:center;top:1220px;font-size:31px">Our Expertise</h2>
<p class="abs" style="left:0;width:1200px;text-align:center;top:1272px;font-size:9.5px">Solutions for every professional firm under Corvanta</p>

<div class="exp-item" style="left:151px"><div class="exp-icon"><span style="background:var(--orange)"></span></div>Business<br>Consulting</div>
<div class="exp-item" style="left:312px"><div class="exp-icon"><span style="background:var(--navy)"></span></div>Training &amp;<br>Courses</div>
<div class="exp-item" style="left:469px"><div class="exp-icon"><span style="background:var(--green)"></span></div>Training &amp;<br>Courses</div>
<div class="exp-item" style="left:628px"><div class="exp-icon"><span style="background:var(--purple)"></span></div>Operational<br>Intelligence</div>
<div class="exp-item" style="left:786px"><div class="exp-icon"><span style="background:var(--orange)"></span></div>Branding<br>&amp; Design</div>
<div class="exp-item" style="left:945px"><div class="exp-icon"><span style="background:var(--green)"></span></div>Business<br>Consulting</div>

<svg class="abs" style="left:0;top:1420px" width="1200" height="90" viewBox="0 0 1200 90" aria-hidden="true" fill="none" stroke="#c9c9c9" stroke-width="1">
  <g fill="#888" stroke="none">
    <circle cx="201" cy="8" r="2.5"/><circle cx="362" cy="8" r="2.5"/><circle cx="519" cy="8" r="2.5"/>
    <circle cx="678" cy="8" r="2.5"/><circle cx="836" cy="8" r="2.5"/><circle cx="995" cy="8" r="2.5"/>
  </g>
  <path d="M201 14v38a10 10 0 0 0 10 10h250"/>
  <path d="M362 14v16a10 10 0 0 0 10 10h90"/>
  <path d="M519 14v60"/>
  <path d="M678 14v60"/>
  <path d="M836 14v16a10 10 0 0 1-10 10h-90"/>
  <path d="M995 14v38a10 10 0 0 1-10 10h-250"/>
</svg>
<div class="dome abs brand">Corvanta</div>

<!-- upskill -->
<h2 class="abs h2" style="left:0;width:1200px;text-align:center;top:1786px;font-size:31px">Upskill Your Team</h2>
<p class="abs body" style="left:310px;width:580px;text-align:center;top:1840px;font-size:9.5px">Corvanta helps your team enhance their skills and stay ahead in a competitive environment. Our professional courses are designed to provide practical knowledge and industry-specific training, enabling employees to improve efficiency, strengthen expertise, and contribute more effectively to your firm's success.</p>

<div class="card" style="left:140px;top:1923px">
  <div class="card__img" role="img" aria-label="Photo of a smiling man with a headset holding a lesson card" style="background:linear-gradient(135deg,#cfd3d6,#7c7f80)"></div>
  <span class="card__tag" style="background:var(--green)">Not Enrolled</span>
  <span class="card__lessons">5 Lessons</span><span class="card__price">$69</span>
  <div class="card__title">Upskill Your Team</div>
  <div class="card__author"><i></i>Author</div>
  <p class="card__text">Boost your team's skills with Corvanta's industry-focused courses for better performance and efficiency.</p>
</div>
<div class="card" style="left:450px;top:1923px">
  <div class="card__img" role="img" aria-label="Photo of a presenter at a whiteboard with a colleague at a laptop" style="background:linear-gradient(135deg,#d9d9d6,#8a8682)"></div>
  <span class="card__tag" style="background:var(--purple)">Not Started</span>
  <span class="card__ring" style="border-color:#d8d8d8">0%</span>
  <span class="card__lessons">7 Lessons</span>
  <div class="card__title">Client Communication Skills</div>
  <div class="card__author"><i></i>Author</div>
  <p class="card__text">Improve your team's client interactions with practical communication skills for stronger relationships and better results.</p>
</div>
<div class="card" style="left:760px;top:1923px">
  <div class="card__img" role="img" aria-label="Photo of students studying together at a table" style="background:linear-gradient(135deg,#c9c0a8,#6d6450)"></div>
  <span class="card__ring">30%</span>
  <span class="card__lessons">10 Lessons</span>
  <div class="card__title">Upskill Your Team</div>
  <div class="card__author"><i></i>Author</div>
  <p class="card__text">Master clear and professional technical documentation to enhance accuracy and efficiency in your work.</p>
</div>
<div class="card" style="left:140px;top:2326px">
  <div class="card__img" role="img" aria-label="Photo of a man with headphones working at a desk beside a plant" style="background:linear-gradient(135deg,#d8d2c4,#7f7667)"></div>
  <span class="card__tag" style="background:var(--purple)">In progress</span>
  <span class="card__ring">75%</span>
  <span class="card__lessons">6 Lessons</span>
  <div class="card__title">Upskill Your Team</div>
  <div class="card__author"><i></i>Author</div>
  <p class="card__text">Boost your team's skills with Corvanta's industry-focused courses for better performance and efficiency.</p>
</div>
<div class="card" style="left:450px;top:2326px">
  <div class="card__img" role="img" aria-label="Photo of two colleagues working on laptops in an office" style="background:linear-gradient(135deg,#d6cfc7,#6e625a)"></div>
  <span class="card__tag" style="background:var(--purple)">In progress</span>
  <span class="card__ring">55%</span>
  <span class="card__lessons">4 Lessons</span>
  <div class="card__title">Client Communication Skills</div>
  <div class="card__author"><i></i>Author</div>
  <p class="card__text">Improve your team's client interactions with practical communication skills for stronger relationships and better results.</p>
</div>
<div class="card" style="left:760px;top:2326px">
  <div class="card__img" role="img" aria-label="Photo of a team reviewing work together at a desk" style="background:linear-gradient(135deg,#b9b1a6,#5b4a40 60%,#c0452e)"></div>
  <span class="card__tag" style="background:var(--yellow)">Complete</span>
  <span class="card__ring">100%</span>
  <span class="card__lessons">8 Lessons</span>
  <div class="card__title">Upskill Your Team</div>
  <div class="card__author"><i></i>Author</div>
  <p class="card__text">Master clear and professional technical documentation to enhance accuracy and efficiency in your work.</p>
</div>
<div class="btn" style="left:536px;top:2742px;width:128px;height:40px">View All Courses</div>

<!-- testimonials -->
<div class="panel" style="top:2880px;height:600px;border-radius:90px 90px 0 0"></div>
<div class="abs ghost-word">Testimonials</div>
<div class="abs quote-card"></div>
<div class="abs quote-photo" role="img" aria-label="Photo of a cheerful man in a white t-shirt pointing to himself"></div>
<div class="abs quote-body" style="left:752px;top:3115px;font-size:42px;font-weight:700;color:var(--ink);line-height:1">&rdquo;</div>
<p class="abs quote-body" style="left:612px;top:3170px;width:320px;text-align:center;font-size:10.5px;line-height:1.75">Corvanta has completely transformed the way our consulting firm manages projects, making our workflows smoother and more efficient. We highly recommend their solutions.</p>
<p class="abs quote-body" style="left:612px;top:3262px;width:320px;text-align:center;font-size:8px;color:var(--muted)">Dale Morrow<br><span style="font-size:7px">CEO Marketing Story</span></p>

<div class="color-band" style="left:0;top:3420px;width:1200px;height:70px" role="img" aria-label="Decorative band of multicoloured geometric shapes"></div>

<!-- call to action -->
<div class="about-photo abs" role="img" aria-label="Photo of a woman presenting at a whiteboard to colleagues in an office" style="top:3596px;background:linear-gradient(135deg,#d3d0ca,#868079 55%,#3f3a36)"></div>
<div class="photo-accent" style="left:567px;top:3853px" role="img" aria-label="Decorative multicoloured accent shape"></div>
<h2 class="abs h2" style="left:705px;top:3665px;width:320px">Ready to elevate your firm?</h2>
<p class="abs body" style="left:705px;top:3752px;width:310px">Get started with Corvanta today and simplify your business operations and team training for greater efficiency and better results.</p>
<div class="btn btn--mix" style="left:700px;top:3816px;width:128px;height:40px">Get Started Now</div>

<!-- footer -->
<div class="panel" style="top:4060px;height:302px;border-radius:70px 70px 0 0"></div>
<div class="abs brand" style="left:130px;top:4140px;font-size:44px">Corvanta<span class="brand__dot" style="width:14px;height:14px"></span></div>
<div class="abs" style="left:130px;top:4262px;display:flex;gap:28px" aria-label="Social links">
  <span style="width:8px;height:8px;border-radius:50%;background:var(--ink)"></span>
  <span style="width:8px;height:8px;border-radius:50%;background:var(--ink)"></span>
  <span style="width:8px;height:8px;border-radius:50%;background:var(--ink)"></span>
  <span style="width:8px;height:8px;border-radius:50%;background:var(--ink)"></span>
  <span style="width:8px;height:8px;border-radius:50%;background:var(--ink)"></span>
</div>
<div class="abs" style="left:387px;top:4128px">
  <div class="foot-h">Company</div>
  <div class="foot-list" style="margin-top:10px">Home<br>About Us<br>Services<br>Courses<br>Contact Us</div>
</div>
<div class="abs" style="left:554px;top:4128px;width:190px;font-size:9.5px;line-height:1.5">
  <div class="foot-h">Contact Us</div>
  <p style="margin-top:18px"><b style="font-weight:600;color:var(--ink)">Phone:</b><br>(555)014-22780</p>
  <p style="margin-top:12px"><b style="font-weight:600;color:var(--ink)">Email:</b><br>hello@corvanta.example</p>
  <p style="margin-top:12px"><b style="font-weight:600;color:var(--ink)">Address:</b><br>Reference site about Lorem Ipsum, giving information on its origins, as</p>
</div>
<div class="abs foot-h" style="left:752px;top:4128px">Subscribe to Our Latest Insights</div>
<div class="abs" style="left:752px;top:4170px;width:317px;height:48px;border-radius:24px;background:#e4e4e4;display:flex;align-items:center;justify-content:space-between;padding:0 22px;font-size:9.5px">
  <span>Your Email Address</span>
  <svg width="12" height="12" viewBox="0 0 12 12" aria-hidden="true"><path d="M1 6l10-5-4 10-1.5-4z" fill="var(--ink)"/></svg>
</div>
<div class="abs" style="left:1112px;top:4306px;width:30px;height:26px;border-radius:50%;background:var(--ink)" aria-label="Chat"></div>
<p class="abs" style="left:0;width:1200px;text-align:center;top:4382px;font-size:9.5px">Copyright © 2026 Corvanta, Inc. All rights reserved.</p>

</body>
</html>
```